Letterhead for SaaS

Design a letterhead that aligns with our new business card, using our logo and color scheme and text defined in the Branding Guide to ensure consistency. Consider incorporating a subtle watermark for added elegance. The layout should reflect the card's style, creating a cohesive look across our stationery.

```html
<!DOCTYPE html>
<html lang="en">
<head>
<meta charset="utf-8">
<title>Veltrion Stationery</title>
<link href="https://fonts.googleapis.com/css2?family=Exo+2:wght@800&family=Josefin+Sans:wght@600&family=Open+Sans:wght@600&display=swap" rel="stylesheet">
<style>
  :root {
    --backdrop: #3b3e41;
    --paper: #ffffff;
    --navy: #0f1829;
    --navy-soft: #1d2b44;
    --sky: #3dbdee;
    --watermark: #ececee;
    --ink: #111722;
    --label: #ffffff;
  }
  * { margin: 0; padding: 0; box-sizing: border-box; }
  html, body { width: 1200px; height: 900px; overflow: hidden; }
  body { background: var(--backdrop); position: relative; font-family: "Josefin Sans", sans-serif; }

  .sheet-label {
    position: absolute;
    font-family: "Open Sans", sans-serif;
    font-weight: 600;
    font-size: 18px;
    color: var(--label);
  }

  .brand-name {
    font-family: "Exo 2", sans-serif;
    font-weight: 800;
    color: var(--ink);
    letter-spacing: 0.02em;
  }
  .brand-dot { display: block; border-radius: 50%; background: var(--navy); }

  .side-band {
    position: absolute; left: 0; top: 0; bottom: 0;
    background: linear-gradient(160deg, var(--navy-soft) 0%, var(--navy) 45%, var(--navy-soft) 75%, var(--navy) 100%);
  }
  .wolf-watermark {
    position: absolute;
    background: radial-gradient(ellipse at 55% 45%, var(--watermark) 0%, #f1f1f3 60%, rgba(255,255,255,0) 100%);
  }

  /* Envelope front */
  .envelope-front {
    position: absolute; left: 76px; top: 310px; width: 455px; height: 197px;
    background: var(--paper); overflow: hidden;
  }
  .envelope-front .side-band { width: 18px; }
  .envelope-front .wolf-watermark { right: 0; top: 4px; width: 136px; height: 190px; }
  .envelope-front .brand-block { position: absolute; left: 34px; top: 14px; display: flex; flex-direction: column; align-items: flex-start; gap: 6px; }
  .envelope-front .brand-dot { width: 22px; height: 22px; }
  .envelope-front .brand-name { font-size: 10px; }
  .envelope-front .return-address {
    position: absolute; left: 9px; top: 172px; display: flex; align-items: center; gap: 5px;
    font-size: 9.5px; color: var(--ink);
  }

  /* Envelope back */
  .envelope-back {
    position: absolute; left: 103px; top: 600px; width: 457px; height: 199px;
    background: var(--paper); overflow: hidden;
  }
  .envelope-back .flap { position: absolute; left: 0; top: 0; width: 457px; height: 74px; }
  .envelope-back .brand-name {
    position: absolute; left: 0; right: 0; top: 44px; text-align: center; font-size: 9px;
  }

  /* Letterhead */
  .letterhead {
    position: absolute; left: 615px; top: 138px; width: 533px; height: 690px;
    background: var(--paper); overflow: hidden;
  }
  .letterhead .side-band { width: 61px; }
  .letterhead .wolf-watermark { left: 64px; top: 19px; width: 380px; height: 650px; }
  .letterhead .brand-block {
    position: absolute; right: 10px; top: 14px; display: flex; flex-direction: column; align-items: flex-end; gap: 10px;
  }
  .letterhead .brand-dot { width: 50px; height: 50px; margin-right: 30px; }
  .letterhead .brand-name { font-size: 16px; }
  .letterhead .contact-list { position: absolute; left: 36px; top: 624px; list-style: none; }
  .letterhead .contact-list li {
    display: flex; align-items: center; gap: 17px; height: 18px;
    font-size: 13px; color: var(--ink);
  }
  .contact-icon { width: 16px; height: 14px; flex: none; }
</style>
</head>
<body>

  <span class="sheet-label" style="left:76px; top:264px;">Envelope Front_4</span>
  <section class="envelope-front">
    <div class="side-band"></div>
    <div class="wolf-watermark" role="img" aria-label="Faint geometric wolf head watermark"></div>
    <div class="brand-block">
      <span class="brand-dot"></span>
      <span class="brand-name">VELTRION</span>
    </div>
    <p class="return-address">
      <svg width="8" height="11" viewBox="0 0 8 11"><path d="M4 0a4 4 0 0 1 4 4c0 3-4 7-4 7S0 7 0 4a4 4 0 0 1 4-4z" fill="var(--sky)"/><circle cx="4" cy="4" r="1.5" fill="var(--navy)"/></svg>
      Maple Ridge, Louisiana 70811, US
    </p>
  </section>

  <span class="sheet-label" style="left:103px; top:554px;">Envelope Back_4</span>
  <section class="envelope-back">
    <svg class="flap" viewBox="0 0 457 74">
      <path d="M0 0H457C450 20 443 35 425 40L232 72Q228 73 224 72L32 40C14 35 7 20 0 0Z" fill="var(--sky)"/>
    </svg>
    <span class="brand-name">VELTRION</span>
  </section>

  <span class="sheet-label" style="left:615px; top:92px;">Letterhead_4</span>
  <section class="letterhead">
    <div class="side-band"></div>
    <div class="wolf-watermark" role="img" aria-label="Large faint geometric wolf head watermark"></div>
    <div class="brand-block">
      <span class="brand-dot"></span>
      <span class="brand-name">VELTRION</span>
    </div>
    <ul class="contact-list">
      <li>
        <svg class="contact-icon" viewBox="0 0 16 14"><path d="M1 5c0-3 14-3 14 0v1h-4V4H5v2H1z M4 7h8l2 6H2z" fill="var(--sky)"/></svg>
        (555) 014-2290
      </li>
      <li>
        <svg class="contact-icon" viewBox="0 0 16 14"><rect x="1" y="2.5" width="14" height="9" fill="none" stroke="var(--sky)" stroke-width="1.4"/><path d="M1 2.5l7 5 7-5M1 11.5l5-4.5M15 11.5l-5-4.5" fill="none" stroke="var(--sky)" stroke-width="1.2"/></svg>
        hello@veltrion.com
      </li>
      <li>
        <svg class="contact-icon" viewBox="0 0 16 14"><circle cx="8" cy="7" r="6.5" fill="var(--sky)"/><path d="M8 0.5v13M1.5 7h13M8 0.5c-3 3-3 10 0 13M8 0.5c3 3 3 10 0 13" fill="none" stroke="var(--navy)" stroke-width="0.9"/></svg>
        www.veltrion.com
      </li>
    </ul>
  </section>

</body>
</html>
```